Vendor Managed Inventory Talking points/Customer hand out

Looking for a single page flyer/Customer handout to be a sell sheet for our Vendor managed Inventory programs
Title: VMI benefits
Risk management:
Identification of Items and values that are sole sourced
Ongoing plans to reduce exposure to sole sourced items
Schedule planning to eliminate freight and outages
Reducing the hidden costs of forecasting errors
(Note; with us managing the point of use we can more accurately forecast)
Managing ever shortening of product lifecycles, minimizing obsolescence
Zero Inventory Exposure:
Minimized or Zero inventory on commodity items
Greatly reducing the Weighted Cost of Capital (WACC)
Reduced WACC can help in calculating Hurdle Rates
True point of use billing:
Allows for better tracking and allocation of expenses from a job-job basis
Custom labeling:
Including things like customer part numbers, exp dates, internal hazmat codes
Insures accurate processes with current materials
Helps to meet 5S requirements
Required for certain audits
Lot tracking/Shelf life:
Active assistance in managing Date Codes/Lot Tracking
Shortened shelf life products identified and managed
Plain statement of expiration dates on products. Calculations are not required
Taken as a whole we can help calculate TRUE management and landed costs of products. Focusing only on the price of items is like looking at just the exposed part of an iceberg. Let RQ7T help you to see what's underneath.
I have attached some other brochures and flyers for style reference
more info on our website too. www.rq7t-example.com
Target Market(s)
Electronics manufacturers
Industry/Entity Type
Electronics
Look and feel

```html
<!DOCTYPE html>
<html lang="en">
<head>
<meta charset="utf-8">
<title>VMI Benefits – RQ7T</title>
<link href="https://fonts.googleapis.com/css2?family=Oswald:wght@500;600&family=Open+Sans:wght@400;700&display=swap" rel="stylesheet">
<style>
  :root {
    --brand-blue: #1b4f93;
    --deep-blue: #123c75;
    --ink: #2e2e2e;
    --dark: #111316;
    --paper-top: #e6e7e9;
    --paper-bottom: #f7f7f7;
    --white: #ffffff;
  }
  * { margin: 0; padding: 0; box-sizing: border-box; }
  html, body { width: 927px; height: 1200px; overflow: hidden; background: var(--white); }
  .flyer {
    position: relative; width: 927px; height: 1200px; overflow: hidden;
    background: linear-gradient(180deg, var(--paper-top) 0%, var(--paper-bottom) 60%, var(--paper-top) 100%);
    font-family: "Open Sans", Arial, sans-serif; color: var(--ink);
  }
  .hero-photo {
    position: absolute; left: 0; top: 0; width: 927px; height: 500px;
    background: linear-gradient(135deg, #2a2d33 0%, #6d7076 30%, #c9cbce 55%, #8b8e93 75%, #e4e5e7 100%);
  }
  .hero-swoosh { position: absolute; left: 0; top: 440px; width: 927px; height: 80px; }
  .title-band {
    position: absolute; left: 134px; top: 466px; width: 659px; height: 113px;
    background: var(--brand-blue); display: flex; align-items: center; justify-content: center;
  }
  .title-band h1 {
    font-family: "Oswald", "Arial Narrow", sans-serif; font-weight: 600;
    font-size: 84px; letter-spacing: 1px; color: var(--white); line-height: 1;
  }
  .column { position: absolute; top: 614px; }
  .column-left { left: 26px; width: 450px; }
  .column-right { left: 480px; width: 430px; }
  .benefit { margin-bottom: 16px; }
  .benefit h2 {
    font-family: "Oswald", "Arial Narrow", sans-serif; font-weight: 500;
    font-size: 27px; color: var(--brand-blue); text-transform: uppercase;
    line-height: 1.1; display: flex; align-items: center; gap: 6px;
  }
  .benefit h2::before {
    content: ""; width: 14px; height: 14px; border-radius: 50%; background: #3a3a3a; flex: none;
  }
  .benefit p { font-size: 15.6px; line-height: 21.6px; margin-left: 19px; }
  .summary {
    position: absolute; left: 42px; top: 985px; width: 850px;
    font-size: 15.6px; line-height: 21.6px;
  }
  .footer-rule { position: absolute; left: 0; top: 1044px; width: 927px; height: 5px; background: var(--dark); }
  .footer {
    position: absolute; left: 0; top: 1056px; width: 927px; height: 144px;
    background: var(--brand-blue); color: var(--white);
  }
  .contact { position: absolute; left: 51px; top: 14px; font-weight: 700; font-size: 48px; line-height: 58px; letter-spacing: 0.5px; }
  .brand-name {
    position: absolute; right: 90px; top: 40px;
    font-family: "Oswald", "Arial Narrow", sans-serif; font-weight: 600; font-size: 56px; color: var(--white);
  }
</style>
</head>
<body>
<div class="flyer">
  <div class="hero-photo" role="img" aria-label="Photo of a parts storeroom with wall-mounted clear plastic bins and small-parts drawer cabinets on shelves"></div>
  <svg class="hero-swoosh" viewBox="0 0 927 80" aria-hidden="true">
    <path d="M0 40 Q300 10 463 20 Q640 10 927 40 L927 80 L0 80 Z" fill="var(--paper-top)"/>
    <path d="M0 30 Q300 0 463 10 Q640 0 927 30 L927 42 Q640 12 463 22 Q300 12 0 42 Z" fill="var(--dark)"/>
    <path d="M0 42 Q300 12 463 22 Q640 12 927 42 L927 50 Q640 20 463 30 Q300 20 0 50 Z" fill="var(--deep-blue)"/>
  </svg>

  <div class="title-band"><h1>VMI BENEFITS</h1></div>

  <div class="column column-left">
    <section class="benefit">
      <h2>Risk Management:</h2>
      <p>Identification of Items and values that are sole sourced<br>
      Ongoing plans to reduce exposure to sole sourced items<br>
      Schedule planning to eliminate freight and outages<br>
      Reducing the hidden costs of forecasting errors<br>
      (Note; with us managing the point of use we can more accurately forecast)<br>
      Managing ever shortening of product lifecycles, minimizing obsolescence</p>
    </section>
    <section class="benefit">
      <h2>Custom Labeling:</h2>
      <p>Including things like customer part numbers, exp dates, internal hazmat codes<br>
      Insures accurate processes with current materials<br>
      Helps to meet 5S requirements<br>
      Required for certain audits</p>
    </section>
  </div>

  <div class="column column-right">
    <section class="benefit">
      <h2>Zero Inventory Exposure:</h2>
      <p>Minimized or Zero inventory on commodity items<br>
      Greatly reducing the Weighted Cost of Capital (WACC)<br>
      Reduced WACC can help in calculating Hurdle Rates</p>
    </section>
    <section class="benefit">
      <h2>True Point of Use Billing:</h2>
      <p>Allows for better tracking and allocation of expenses from a job-job basis</p>
    </section>
    <section class="benefit">
      <h2>Lot Tracking/Shelf Life:</h2>
      <p>Active assistance in managing Date Codes/Lot Tracking Shortened shelf life products identified and managed Plain statement of expiration dates on products. Calculations are not required</p>
    </section>
  </div>

  <p class="summary">Taken as a whole we can help calculate TRUE management and landed costs of products. Focusing only on the price of items is like looking at just the exposed part of an iceberg. Let RQ7T help you to see what's underneath.</p>

  <div class="footer-rule"></div>
  <footer class="footer">
    <div class="contact">www.rq7t-example.com<br>800.555.0147</div>
    <div class="brand-name">RQ7T</div>
  </footer>
</div>
</body>
</html>
```